Baron of Bones mobile game for IOS and Android

We need all screens designed for a multiplayer craps app. Please see the attached document describing features and some similar app styles I am looking for. I have also included the prototype of the app in HTML. We would like the app to be design to be compatible on phones or tablets.

In regards to the prototypes, this is just a general idea of how I'd like the layout. For the most part, all of the elements on each screen should be there but I don't necessarily care that they are in the same position(s) as in the prototype. In fact, I would prefer that you don't just follow this as a guide and think outside the box a bit.

I think it is fine for the initial entry to only contain just a subset of the required screens (just main lobby and game table screen) rather than all designers having to submit a design containing all screens for the full app. The remaining screens can then be finished using the same style in the design handover phase of this project. This will give me an idea of the design you have in mind without extra work to all the non-winning bidders.

If you have any questions about this project, please ask.

Good Luck!

Target Market(s)

Casual gamers

Industry/Entity Type

Games

Font styles to use
Sans Serif

Requirements
Must have
• All of the main screens shown in the prototype in the uploads.
Nice to have
• The additional popup screens described in the document.
Should not have
• Content copied from other apps, images requiring license

```html
<!DOCTYPE html>
<html lang="en">
<head>
<meta charset="utf-8">
<title>Baron of Bones – Craps Table</title>
<link href="https://fonts.googleapis.com/css2?family=Montserrat:wght@600;700;800&family=Kaushan+Script&family=Fredoka:wght@500;600&display=swap" rel="stylesheet">
<style>
:root{
  --bg:#2f2f2f;
  --felt:#0e7a3c;
  --felt-dark:#0a6431;
  --rim:#c8b07a;
  --rim-dark:#a88f58;
  --cushion:#ececec;
  --line:#ffffff;
  --gold:#f4d21a;
  --red:#e3202a;
  --red-dark:#a9121a;
  --yellow-btn:#f7c315;
  --tag:#1b1b1b;
  --chip-green:#1a9b3a;
  --chip-blue:#2a8fd6;
  --chip-red:#d3222a;
  --chip-black:#202020;
}
html,body{margin:0;padding:0;overflow:hidden;background:var(--bg);}
.game-table{display:block;width:1200px;height:675px;}
.label{font-family:"Montserrat",sans-serif;}
.num{font-family:"Montserrat",sans-serif;font-weight:800;fill:var(--gold);}
.script{font-family:"Kaushan Script",cursive;fill:var(--gold);}
.white{fill:var(--line);}
.red-text{fill:var(--red);font-family:"Montserrat",sans-serif;font-weight:700;}
.lines{fill:none;stroke:var(--line);stroke-width:3;}
.tag-text{font-family:"Montserrat",sans-serif;font-size:15px;fill:#555;}
.ui-text{font-family:"Fredoka",sans-serif;}
.chip-mark{font-family:"Montserrat",sans-serif;font-weight:800;font-size:17px;fill:var(--gold);text-anchor:middle;}
</style>
</head>
<body>
<svg class="game-table" viewBox="0 0 1280 720" xmlns="http://www.w3.org/2000/svg">
  <defs>
    <radialGradient id="feltGrad" cx="50%" cy="50%" r="60%">
      <stop offset="0" stop-color="#13894a"/>
      <stop offset="1" stop-color="var(--felt-dark)"/>
    </radialGradient>
    <g id="chip">
      <circle r="20" fill="currentColor"/>
      <circle r="20" fill="none" stroke="#fff" stroke-width="4" stroke-dasharray="6 6"/>
      <circle r="13" fill="currentColor" stroke="#fff" stroke-width="1.5"/>
      <text class="chip-mark" y="6">$</text>
    </g>
    <g id="avatar">
      <rect x="-32" y="-32" width="64" height="64" rx="4" fill="#8a8a8a" stroke="#ddd" stroke-width="2"/>
      <circle r="26" fill="#fff"/>
      <circle cy="-7" r="9" fill="none" stroke="var(--red)" stroke-width="3"/>
      <path d="M-15 15 a15 12 0 0 1 30 0 Z" fill="none" stroke="var(--red)" stroke-width="3"/>
    </g>
    <g id="tag">
      <rect x="0" y="-11" width="95" height="22" rx="11" fill="var(--tag)" stroke="#ccc" stroke-width="1.5"/>
    </g>
  </defs>

  <!-- table -->
  <g class="table">
    <rect x="95" y="93" width="1172" height="516" rx="258" fill="var(--rim)"/>
    <rect x="107" y="105" width="1148" height="492" rx="246" fill="var(--cushion)"/>
    <rect x="122" y="118" width="1118" height="466" rx="233" fill="var(--rim-dark)"/>
    <rect x="128" y="124" width="1106" height="454" rx="227" fill="url(#feltGrad)"/>
  </g>

  <!-- betting layout -->
  <g class="layout">
    <path class="lines" d="M250 162 H562 M250 188 H1085 M250 162 V290 M313 162 V290 M375 162 V290 M438 162 V290 M500 162 V290 M562 162 V530 M622 215 V290 M250 215 H622 M250 290 H622 M175 215 H250 V290 H175 Z"/>
    <path class="lines" d="M265 290 V397 H562 M180 430 L265 397 M265 397 L312 480 V530 H562 M300 397 V480 H562 M160 410 Q170 520 240 540 L560 540"/>
    <text class="num" x="281" y="272" font-size="46" text-anchor="middle">4</text>
    <text class="num" x="344" y="272" font-size="46" text-anchor="middle">5</text>
    <text class="script" x="406" y="266" font-size="28" text-anchor="middle" transform="rotate(-12 406 258)">Six</text>
    <text class="num" x="469" y="272" font-size="46" text-anchor="middle">8</text>
    <text class="script" x="530" y="266" font-size="26" text-anchor="middle" transform="rotate(-20 530 258)">Nine</text>
    <text class="num" x="592" y="268" font-size="36" text-anchor="middle">10</text>
    <text class="red-text" x="222" y="235" font-size="14" text-anchor="middle">DONT</text>
    <text class="red-text" x="222" y="256" font-size="14" text-anchor="middle">COME</text>
    <text class="red-text" x="222" y="277" font-size="14" text-anchor="middle">BAR</text>
    <text class="label white" x="412" y="367" font-size="60" font-weight="700" text-anchor="middle">COME</text>
    <text class="label white" x="245" y="460" font-size="30" font-weight="600" text-anchor="middle" transform="rotate(65 245 455)">6 / 8</text>
    <g class="label white" font-size="21" font-weight="600" text-anchor="middle">
      <circle cx="321" cy="431" r="13" class="lines" stroke-width="2"/><text x="321" y="439">2</text>
      <text x="351" y="439">3</text><text x="379" y="439">4</text><text x="408" y="439">9</text>
      <text x="445" y="439">10</text><text x="489" y="439">11</text>
      <circle cx="533" cy="431" r="15" class="lines" stroke-width="2"/><text x="533" y="439">12</text>
    </g>
    <text class="red-text" x="429" y="462" font-size="18" text-anchor="middle">FIELD</text>
    <text class="red-text" x="443" y="512" font-size="18" text-anchor="middle">DONT PASS BAR</text>
    <text class="label white" x="420" y="553" font-size="14" font-weight="700" text-anchor="middle">PASS LINE</text>
  </g>

  <!-- proposition bets -->
  <g class="props">
    <rect class="lines" x="808" y="202" width="260" height="326" rx="20"/>
    <path class="lines" d="M808 228 H1068 M808 297 H1068 M808 365 H1068 M808 435 H1068 M808 503 H1068 M932 228 V365 M932 435 V503 M880 365 V435 M995 365 V435"/>
    <g class="label white" font-size="20" font-weight="600" text-anchor="middle">
      <text x="852" y="222">5 to 1</text><text x="1025" y="222">5 to 1</text>
      <text x="870" y="286">10 to 1</text><text x="1000" y="288">8 to 1</text>
      <text x="870" y="355">10 to 1</text><text x="1000" y="355">8 to 1</text>
      <text x="844" y="425">16 to 1</text><text x="938" y="425">31 to 1</text><text x="1032" y="425">31 to 1</text>
      <text x="870" y="495">16 to 1</text><text x="1000" y="495">16 to 1</text>
      <text x="850" y="523">8 to 1</text><text x="1030" y="523">8 to 1</text>
    </g>
    <text class="red-text" x="935" y="222" font-size="14" text-anchor="middle">SEVEN</text>
    <text class="red-text" x="940" y="522" font-size="14" text-anchor="middle">ANY CRAPS</text>
    <g fill="var(--gold)">
      <rect x="852" y="241" width="13" height="13"/><rect x="877" y="241" width="13" height="13"/>
      <rect x="983" y="241" width="13" height="13"/><rect x="1008" y="241" width="13" height="13"/>
      <rect x="852" y="310" width="13" height="13"/><rect x="877" y="310" width="13" height="13"/>
      <rect x="983" y="310" width="13" height="13"/><rect x="1008" y="310" width="13" height="13"/>
      <rect x="828" y="382" width="13" height="13"/><rect x="849" y="382" width="13" height="13"/>
      <rect x="913" y="382" width="13" height="13"/><rect x="938" y="382" width="13" height="13"/>
      <rect x="1016" y="382" width="13" height="13"/><rect x="1038" y="382" width="13" height="13"/>
      <rect x="852" y="453" width="13" height="13"/><rect x="877" y="453" width="13" height="13"/>
      <rect x="983" y="453" width="13" height="13"/><rect x="1008" y="453" width="13" height="13"/>
    </g>
    <g class="label white" font-size="15" font-weight="700" text-anchor="middle" fill="none">
      <g stroke="#fff" stroke-width="2" fill="none">
        <circle cx="758" cy="218" r="12"/><circle cx="758" cy="262" r="12"/><circle cx="758" cy="304" r="12"/>
        <circle cx="758" cy="346" r="12"/><circle cx="758" cy="388" r="12"/><circle cx="758" cy="430" r="12"/><circle cx="758" cy="472" r="12"/>
        <circle cx="790" cy="240" r="12"/><circle cx="790" cy="276" r="12"/><circle cx="790" cy="314" r="12"/>
        <circle cx="790" cy="348" r="12"/><circle cx="790" cy="382" r="12"/><circle cx="790" cy="418" r="12"/><circle cx="790" cy="454" r="12"/>
      </g>
      <g fill="#fff">
        <text x="758" y="223">E</text><text x="758" y="267">E</text><text x="758" y="309">E</text><text x="758" y="351">E</text>
        <text x="758" y="393">E</text><text x="758" y="435">E</text><text x="758" y="477">E</text>
        <text x="790" y="245">C</text><text x="790" y="281">C</text><text x="790" y="319">C</text><text x="790" y="353">C</text>
        <text x="790" y="387">C</text><text x="790" y="423">C</text><text x="790" y="459">C</text>
      </g>
    </g>
  </g>

  <!-- chips on table -->
  <g class="table-chips">
    <use href="#chip" x="282" y="207" style="color:var(--chip-blue)" transform="translate(282 207) scale(.75) translate(-282 -207)"/>
    <use href="#chip" x="460" y="207" style="color:var(--chip-red)" transform="translate(460 207) scale(.75) translate(-460 -207)"/>
    <use href="#chip" x="946" y="336" style="color:var(--chip-blue)" transform="translate(946 336) scale(.75) translate(-946 -336)"/>
    <g transform="translate(0 0)">
      <use href="#chip" x="607" y="155" style="color:var(--chip-green)"/><use href="#chip" x="607" y="170" style="color:var(--chip-green)"/><use href="#chip" x="607" y="184" style="color:var(--chip-green)"/>
      <use href="#chip" x="643" y="155" style="color:var(--chip-blue)"/><use href="#chip" x="643" y="170" style="color:var(--chip-blue)"/><use href="#chip" x="643" y="184" style="color:var(--chip-blue)"/>
      <use href="#chip" x="699" y="155" style="color:var(--chip-red)"/><use href="#chip" x="699" y="170" style="color:var(--chip-red)"/><use href="#chip" x="699" y="184" style="color:var(--chip-red)"/>
      <use href="#chip" x="735" y="155" style="color:var(--chip-black)"/><use href="#chip" x="735" y="170" style="color:var(--chip-black)"/><use href="#chip" x="735" y="184" style="color:var(--chip-black)"/>
    </g>
  </g>

  <!-- dealer seat -->
  <g class="dealer-seat">
    <rect x="618" y="3" width="105" height="99" rx="6" fill="#8a8a8a" stroke="#ddd" stroke-width="3"/>
    <circle cx="670" cy="52" r="37" fill="#ddd" stroke="#fff" stroke-width="4"/>
  </g>

  <!-- players -->
  <g class="players">
    <g><use href="#tag" x="170" y="139"/><use href="#avatar" x="210" y="97"/><use href="#chip" x="156" y="136" style="color:var(--chip-blue)"/><text class="tag-text" x="210" y="145" fill="#3a7bb8">2145</text></g>
    <g><use href="#tag" x="375" y="107"/><use href="#avatar" x="416" y="63"/><use href="#chip" x="366" y="104" style="color:var(--chip-green)"/><text class="tag-text" x="412" y="113">2145</text></g>
    <g><use href="#tag" x="810" y="113"/><use href="#avatar" x="860" y="70"/><use href="#chip" x="910" y="115" style="color:var(--chip-green)"/><text class="tag-text" x="825" y="119">2145</text></g>
    <g><use href="#tag" x="993" y="126"/><use href="#avatar" x="1047" y="83"/><use href="#chip" x="1100" y="126" style="color:var(--chip-red)"/><text class="tag-text" x="1010" y="132" fill="var(--red)">2145</text></g>
    <g><use href="#tag" x="1131" y="181"/><use href="#avatar" x="1186" y="137"/><use href="#chip" x="1236" y="180" style="color:var(--chip-green)"/><text class="tag-text" x="1150" y="187">2145</text></g>
    <g><use href="#tag" x="68" y="275"/><use href="#avatar" x="108" y="231"/><use href="#chip" x="55" y="273" style="color:var(--chip-red)"/><use href="#chip" x="186" y="273" style="color:var(--chip-red)" transform="translate(186 273) scale(.75) translate(-186 -273)"/><text class="tag-text" x="104" y="281">2145</text></g>
    <g><use href="#tag" x="115" y="500"/><use href="#avatar" x="161" y="455"/><use href="#chip" x="110" y="500" style="color:var(--chip-black)"/><text class="tag-text" x="150" y="506">2145</text></g>
    <g><use href="#tag" x="1150" y="538"/><use href="#avatar" x="1210" y="497"/><use href="#chip" x="1257" y="538" style="color:var(--chip-blue)"/><text class="tag-text" x="1172" y="545" fill="#3a7bb8">2145</text></g>
  </g>

  <!-- corner buttons -->
  <g class="corner-buttons">
    <circle cx="48" cy="48" r="32" fill="var(--red)" stroke="#fff" stroke-width="3"/>
    <path d="M48 28 V64 M34 52 L48 66 L62 52" fill="none" stroke="#fff" stroke-width="7" stroke-linecap="round" stroke-linejoin="round"/>
    <circle cx="1232" cy="48" r="32" fill="var(--red)" stroke="#fff" stroke-width="3"/>
    <path d="M1219 35 L1245 61 M1245 35 L1219 61" stroke="#fff" stroke-width="8" stroke-linecap="round"/>
  </g>

  <!-- side menu -->
  <g class="side-menu">
    <rect x="20" y="362" width="60" height="300" rx="30" fill="#1c1c1c" stroke="#ddd" stroke-width="2"/>
    <g fill="var(--yellow-btn)" stroke="#fff" stroke-width="3">
      <circle cx="50" cy="408" r="28"/><circle cx="50" cy="490" r="28"/><circle cx="50" cy="570" r="28"/>
    </g>
    <text class="ui-text" x="50" y="420" font-size="32" font-weight="600" fill="#fff" text-anchor="middle">?</text>
    <path d="M45 502 V478 L58 475 V497" fill="none" stroke="#fff" stroke-width="4"/><circle cx="41" cy="502" r="5" fill="#fff"/><circle cx="54" cy="497" r="5" fill="#fff"/>
    <path d="M38 564 H45 L54 556 V584 L45 576 H38 Z" fill="#fff"/><path d="M59 562 q7 8 0 16" fill="none" stroke="#fff" stroke-width="3"/>
    <circle cx="48" cy="668" r="38" fill="var(--red)" stroke="#fff" stroke-width="3"/>
    <circle cx="48" cy="668" r="13" fill="none" stroke="#fff" stroke-width="9" stroke-dasharray="5 3.2"/>
    <circle cx="48" cy="668" r="5" fill="var(--red)"/>
  </g>

  <!-- bottom bar -->
  <g class="bottom-bar">
    <rect x="370" y="648" width="210" height="40" rx="20" fill="#111" stroke="#ddd" stroke-width="2"/>
    <use href="#chip" x="385" y="668" style="color:var(--chip-green)"/>
    <text class="ui-text" x="552" y="680" font-size="30" fill="#fff" text-anchor="end">2145</text>
    <circle cx="580" cy="668" r="18" fill="var(--red)" stroke="#fff" stroke-width="2"/>
    <path d="M580 659 V677 M571 668 H589" stroke="#fff" stroke-width="4"/>
    <circle cx="670" cy="665" r="52" fill="#fff"/><circle cx="670" cy="665" r="44" fill="var(--yellow-btn)"/>
    <g transform="rotate(-15 655 665)"><rect x="640" y="650" width="28" height="28" rx="4" fill="#9fd04f"/></g>
    <g transform="rotate(15 685 660)"><rect x="672" y="646" width="28" height="28" rx="4" fill="#9fd04f"/></g>
    <rect x="772" y="647" width="185" height="56" rx="16" fill="var(--yellow-btn)" stroke="#e09a00" stroke-width="3"/>
    <text class="ui-text" x="864" y="688" font-size="32" font-weight="600" fill="#a0411a" text-anchor="middle">BET</text>
    <rect x="1062" y="658" width="174" height="44" fill="#e6e6e6"/>
    <text class="ui-text" x="1149" y="692" font-size="30" font-weight="500" fill="#a31b1b" text-anchor="middle">2145</text>
    <circle cx="1052" cy="607" r="24" fill="var(--red)" stroke="#fff" stroke-width="2"/>
    <path d="M1058 595 L1046 607 L1058 619" fill="none" stroke="#fff" stroke-width="4"/>
    <use href="#chip" x="1139" y="607" style="color:var(--chip-red)"/>
    <circle cx="1228" cy="607" r="24" fill="var(--red)" stroke="#fff" stroke-width="2"/>
    <path d="M1222 595 L1234 607 L1222 619" fill="none" stroke="#fff" stroke-width="4"/>
  </g>
</svg>
</body>
</html>
```